An envelope for Housekeepers / The Marigold Sleeve

Globally, 212 million people are employed in the hospitality industry. While many get commemorated for their work, there is one job that is often looked over.
Housekeepers hardly ever get told how great of a job they are doing.
Our company QuillNestly is seeking to empower housekeepers by allowing our guests to tip them through a cool envelope.
The plan :
- Create an envelope that has a message on it, which will incentivize our clientele to tip their housekeepers at check-out, and give housekeepers the credit they deserve for their hard work.
Example :
- "Humans do well by doing good" / "a thank you for your housekeeper"
What to do :
- Create an envelope based on the attached file. The white page titled "The Marigold Sleeve" will be the front of the envelope (feel free to improve it but we really like the concept of it). The four blue pages will be the back pages of the envelope. Feel free to scour the web for quotes & embodying the same message of generosity.
We are really looking forward to seeing what kind of creative envelope you can conjure.
PS : remember that the goal with this envelope is to empower housekeepers & incentivize guests to tip them.
Target Market(s)
Travelers & housekeepers
Industry/Entity Type
Hospitality
Other font styles liked:
- Trebuchet, Times New Roman
Requirements
Must have
- Our project must have :
- - A white first page titled "The Marigold Sleev" is a must
- - You can improve it, but do not change the concept of it
- - Font : simple & easy to read
- - Color of back page : Teal
Nice to have
- Always keep in mind that this envelope is made to empower housekeepers.
Should not have
- Just keep it simple. Don't complicate things.

```html
<!DOCTYPE html>
<html lang="en">
<head>
<meta charset="utf-8">
<title>The Marigold Sleev — Envelope Front and Back</title>
<link rel="stylesheet" href="https://fonts.googleapis.com/css2?family=Jost:wght@400;500;600&display=swap">
<style>
  :root {
    --backdrop: #474747;
    --paper: #ffffff;
    --teal: #acdddd;
    --ink-grey: #555555;
    --ink-white: #ffffff;
  }
  * { margin: 0; padding: 0; box-sizing: border-box; }
  html, body {
    width: 1189px;
    height: 1200px;
    overflow: hidden;
  }
  body {
    background: var(--backdrop);
    font-family: "Jost", "Trebuchet MS", sans-serif;
    position: relative;
  }
  .envelope-face {
    position: absolute;
  }
  .envelope-front {
    left: 75px;
    top: 163px;
    width: 436px;
    height: 904px;
    background: var(--paper);
  }
  .envelope-back {
    left: 669px;
    top: 166px;
    width: 433px;
    height: 899px;
    background: var(--teal);
  }
  .centered-line {
    position: absolute;
    left: 0;
    width: 100%;
    text-align: center;
    white-space: nowrap;
  }

  /* Front */
  .front-title {
    color: var(--teal);
    font-weight: 600;
    font-size: 46px;
    line-height: 60px;
    letter-spacing: 0.33em;
    padding-left: 0.33em;
    text-transform: uppercase;
  }
  .front-title.line-1 { top: 350px; }
  .front-title.line-2 { top: 419px; }
  .front-title.line-3 { top: 491px; }

  .brand-lockup {
    position: absolute;
    left: 0;
    width: 100%;
    top: 805px;
    display: flex;
    justify-content: center;
    align-items: center;
    gap: 12px;
  }
  .brand-dot {
    width: 50px;
    height: 50px;
    border: 3px solid var(--ink-grey);
    border-radius: 50%;
  }
  .brand-name {
    color: var(--ink-grey);
    font-weight: 500;
    font-size: 26px;
    line-height: 23px;
    text-transform: uppercase;
  }

  /* Back */
  .quote-line {
    color: var(--ink-white);
    font-weight: 600;
    font-size: 35px;
    line-height: 48px;
    letter-spacing: 0.01em;
  }
  .quote-line.line-1 { top: 313px; }
  .quote-line.line-2 { top: 362px; }
  .quote-line.line-3 { top: 410px; }
  .quote-line.line-4 { top: 457px; }

  .quote-subline {
    top: 541px;
    color: var(--ink-white);
    font-weight: 600;
    font-size: 20px;
    line-height: 24px;
    letter-spacing: 0.05em;
  }

  .tagline {
    color: var(--ink-white);
    font-weight: 500;
    font-size: 26px;
    line-height: 29px;
    text-transform: uppercase;
  }
  .tagline.line-1 { top: 795px; }
  .tagline.line-2 { top: 824px; }
</style>
</head>
<body>

  <section class="envelope-face envelope-front" aria-label="Envelope front">
    <h1>
      <span class="centered-line front-title line-1">The</span>
      <span class="centered-line front-title line-2">Marigold</span>
      <span class="centered-line front-title line-3">Sleev</span>
    </h1>
    <div class="brand-lockup">
      <span class="brand-dot" aria-hidden="true"></span>
      <span class="brand-name">Quill<br>Nestly</span>
    </div>
  </section>

  <section class="envelope-face envelope-back" aria-label="Envelope back">
    <blockquote>
      <p class="centered-line quote-line line-1">“GENEROSITY</p>
      <p class="centered-line quote-line line-2">ISN’T AN ACT.</p>
      <p class="centered-line quote-line line-3">IT’S A WAY OF LIFE.”</p>
      <p class="centered-line quote-line line-4">DALE WRENFIELD</p>
    </blockquote>
    <p class="centered-line quote-subline">Humans Do Well by Doing Good</p>
    <p class="centered-line tagline line-1">Resting</p>
    <p class="centered-line tagline line-2">Redefined</p>
  </section>

</body>
</html>
```